Investor Information Presentation Design Required and Corporate overview design

I have all the materials ready to go, just need 1x Pro Design for the presentation and 1x Pro Design for the corporate overview.
I am ok with images being changed (only if it represents the company better). Wording Can NOT be changed. Any process diagrams can be changed to better represent the process.
I can provide high res Logo file and obviously the files for the presentation and corporate overview. What I have done is basic, but need it to look far more polished and professional.

Target Market(s)

Fixed Term Deposits - $100,000 + High interest rates

Industry/Entity Type

Investment

Font styles to use
Sans Serif

Requirements
Must have
• A corporate professional look, think banks, financial services, business etc
• The presentation is NOT used for group presenting purposes - Individuals go through it on their own. Should want to make me feel like I have to read it all!

```html
<!DOCTYPE html>
<html lang="en">
<head>
<meta charset="utf-8">
<title>Meridian Capital – High Yield Term Deposits</title>
<link href="https://fonts.googleapis.com/css2?family=Open+Sans:wght@300;400;600;700&display=swap" rel="stylesheet">
<style>
:root{
  --navy:#2b2a6b;
  --blue:#1f9fe0;
  --sky:#4db6ea;
  --grey:#9a9ba6;
  --ink:#3a3a44;
  --text:#55565f;
  --page:#ffffff;
}
*{box-sizing:border-box;margin:0;padding:0}
html,body{width:1200px;height:701px;overflow:hidden;background:var(--page)}
body{position:relative;font-family:"Open Sans",Arial,sans-serif;color:var(--text)}
.slide{position:absolute;width:392px;height:221px;background:#fff;overflow:hidden;box-shadow:0 1px 4px rgba(0,0,0,.22)}
.c1{left:4px}.c2{left:404px}.c3{left:804px}
.r1{top:10px}.r2{top:240px}.r3{top:470px}
.abs{position:absolute}
.photo{position:absolute}
/* footer */
.foot{position:absolute;left:0;bottom:0;width:100%;height:11px;display:flex}
.foot-bar{flex:1;background:var(--blue);color:#fff;font-size:3.6px;display:flex;justify-content:space-between;align-items:center;padding:0 8px 0 8px}
.foot-num{width:14px;background:#fff;font-size:4px;color:#777;display:flex;align-items:center;justify-content:center}
.foot-end{width:14px;background:var(--navy)}
/* brand */
.brand{position:absolute;top:13px;right:12px;display:flex;align-items:center;gap:3px;font-size:6.5px;font-weight:600;color:var(--navy)}
.brand::before{content:"";width:9px;height:9px;border-radius:50%;background:var(--blue)}
.brand.light{color:#fff}
.brand.light::before{background:#fff}
/* title */
.title{position:absolute;font-size:16px;font-weight:400;color:var(--ink);line-height:1}
.title::after{content:"";position:absolute;left:0;bottom:-5px;width:28px;height:2px;background:var(--blue)}
/* icon list */
.ic{position:absolute;width:12px;height:12px;border-radius:50%;display:flex;align-items:center;justify-content:center}
.ic svg{width:7px;height:7px}
.ic.navy{background:var(--navy)}.ic.blue{background:var(--blue)}.ic.grey{background:var(--grey)}
.item{position:absolute;font-size:6.2px;line-height:1.35;color:var(--text)}
/* cover */
.cover-bg{inset:0;background:linear-gradient(135deg,#ffffff 0%,#eef2f7 45%,#e3e9f1 100%)}
.cover-name{position:absolute;left:0;width:100%;top:140px;text-align:center;font-size:28px;font-weight:600;letter-spacing:2px;color:var(--navy)}
.cover-name::before{content:"";display:block;width:40px;height:40px;border-radius:50%;background:var(--blue);margin:-56px auto 14px}
.cover-sub{position:absolute;left:0;width:100%;top:182px;text-align:center;font-size:8.5px;color:var(--navy)}
/* slide 2 */
.tower{inset:0;background:linear-gradient(175deg,#cfdbe7 0%,#8fa6bd 40%,#4f6a86 100%)}
.band{position:absolute;left:0;top:141px;width:100%;height:43px;background:rgba(31,159,224,.9);color:#fff;font-size:17px;display:flex;align-items:center;justify-content:center}
.brand-box{position:absolute;top:0;right:12px;width:50px;height:40px;background:#fff;display:flex;align-items:flex-end;justify-content:center;padding-bottom:5px;font-size:6px;font-weight:600;color:var(--navy)}
/* table */
.rates{position:absolute;left:12px;top:62px;width:184px;height:122px;background:#f4f5f8;box-shadow:0 1px 3px rgba(0,0,0,.15)}
.rates .hd{position:absolute;top:0;height:44px;color:#fff;font-size:6px;font-weight:600;display:flex;align-items:center;justify-content:center;text-align:center;line-height:1.3}
.rates .row{position:absolute;left:0;width:100%;font-size:6.3px;color:var(--ink)}
.rates .row span{position:absolute}
/* notes */
.note-h{position:absolute;left:208px;top:51px;font-size:6.5px;font-weight:600;color:var(--ink)}
/* quotes */
.quote{position:absolute;left:156px;width:226px;font-size:5.3px;line-height:1.35;color:var(--text)}
.by{display:block;text-align:right;color:var(--blue)}
.aside{display:block;text-align:right;color:var(--blue);margin-top:1px}
/* team */
.mgr{position:absolute;top:52px;width:52px;text-align:center}
.mgr .head{width:38px;height:38px;border-radius:50%;border:2px solid var(--blue);margin:0 auto;background:linear-gradient(180deg,#d9dde3,#8b929c)}
.mgr .nm{font-size:4.8px;color:var(--ink);margin-top:3px;line-height:1.2}
.mgr .rl{font-size:3.8px;color:var(--blue);line-height:1.2}
.mgr .lk{font-size:3.6px;color:var(--navy);text-decoration:underline;margin-top:2px}
.mgr ul{list-style:none;text-align:left;font-size:3.6px;line-height:1.3;margin-top:5px;padding-left:3px}
.mgr li{margin-bottom:2px;padding-left:4px;position:relative}
.mgr li::before{content:"";position:absolute;left:0;top:1.6px;width:1.6px;height:1.6px;border-radius:50%;background:var(--ink)}
/* get started */
.start-bg{position:absolute;left:136px;top:0;width:256px;height:112px;background:linear-gradient(90deg,#3aa9e3,#8fd0f2)}
.contact{position:absolute;font-size:4.2px;line-height:1.35;color:var(--ink)}
.contact b{font-weight:700;display:block}
.contact a{color:var(--blue);text-decoration:underline}
</style>
</head>
<body>

<!-- 1 Cover -->
<section class="slide c1 r1">
  <div class="photo cover-bg" role="img" aria-label="Faint background of financial charts and paperwork"></div>
  <div class="cover-name">Meridian Capital</div>
  <div class="cover-sub">High Yield Term Deposits</div>
</section>

<!-- 2 Title -->
<section class="slide c2 r1">
  <div class="photo tower" role="img" aria-label="Glass office tower photographed from below against the sky"></div>
  <div class="brand-box">Meridian Capital</div>
  <div class="band">High Yield Term Deposits</div>
  <div class="foot"><div class="foot-bar"><span>Meridian Capital Pty Ltd ACN: 512 448 730</span><span>Head Office: Suite 8.04 Harbourview House, 220 Quay St, Melbourne 3008 VIC</span></div><div class="foot-num" style="width:50px;color:#888">November 28, 2016</div><div class="foot-end"></div></div>
</section>

<!-- 3 Problem -->
<section class="slide c3 r1">
  <div class="brand">Meridian Capital</div>
  <h2 class="title" style="left:20px;top:20px">The Problem</h2>
  <div class="photo" style="left:18px;top:61px;width:178px;height:118px;background:linear-gradient(120deg,#2d3440,#6d7886 55%,#d7dde4)" role="img" aria-label="Businessman in a suit looking thoughtful"></div>
  <div class="ic navy" style="left:211px;top:75px"><svg viewBox="0 0 10 10"><rect x="2" y="1" width="6" height="8" fill="#fff"/></svg></div>
  <p class="item" style="left:234px;top:74px;width:140px">Term deposits with leading banks pay less than 4.0% per annum</p>
  <div class="ic blue" style="left:211px;top:119px"><svg viewBox="0 0 10 10"><path d="M1 3 L5 6 L9 8" stroke="#fff" stroke-width="1.5" fill="none"/></svg></div>
  <p class="item" style="left:234px;top:121px;width:140px">Savings are getting eroded by inflation</p>
  <div class="ic grey" style="left:211px;top:165px"><svg viewBox="0 0 10 10"><rect x="1" y="3" width="8" height="6" fill="#fff"/></svg></div>
  <p class="item" style="left:234px;top:164px;width:140px">Banks continue to profit despite paying low rates of return</p>
  <div class="foot"><div class="foot-bar"><span>Meridian Capital Pty Ltd ACN: 512 448 730</span><span>Head Office: Suite 8.04 Harbourview House, 220 Quay St, Melbourne 3008 VIC</span></div><div class="foot-num">3</div><div class="foot-end"></div></div>
</section>

<!-- 4 Solution -->
<section class="slide c1 r2">
  <div class="photo" style="left:0;top:0;width:196px;height:221px;background:linear-gradient(135deg,#d8d8d8,#a9a9a9 60%,#c8c8c8)" role="img" aria-label="Rising bar chart with a red arrow curving upward"></div>
  <div class="brand">Meridian Capital</div>
  <h2 class="title" style="left:213px;top:30px">The Solution</h2>
  <p class="abs" style="left:213px;top:60px;width:165px;font-size:8px;font-weight:700;color:var(--navy);line-height:1.4">Place your money with Meridian Capital to benefit from -</p>
  <div class="ic blue" style="left:189px;top:94px;width:16px;height:16px"><svg viewBox="0 0 10 10"><path d="M2 8V6M5 8V4M8 8V2" stroke="#fff" stroke-width="1.6"/></svg></div>
  <p class="item" style="left:213px;top:97px;font-weight:600;color:var(--navy)">A fixed, high rate of return</p>
  <div class="ic navy" style="left:189px;top:124px;width:16px;height:16px"><svg viewBox="0 0 10 10"><circle cx="5" cy="5" r="3.5" stroke="#fff" fill="none"/><path d="M5 3V5L6.5 6" stroke="#fff" fill="none"/></svg></div>
  <p class="item" style="left:213px;top:127px;font-weight:600;color:var(--navy)">Quarterly interest payments</p>
  <div class="ic blue" style="left:189px;top:154px;width:16px;height:16px"><svg viewBox="0 0 10 10"><path d="M1 8L4 5L6 6L9 2" stroke="#fff" stroke-width="1.4" fill="none"/></svg></div>
  <p class="item" style="left:213px;top:157px;font-weight:600;color:var(--navy)">Keeping ahead of inflation</p>
  <div class="ic grey" style="left:189px;top:185px;width:16px;height:16px"><svg viewBox="0 0 10 10"><path d="M2 7H8L9 3L6.5 5L5 2L3.5 5L1 3Z" fill="#fff"/></svg></div>
  <p class="item" style="left:213px;top:185px;width:150px;font-weight:600;color:var(--navy)">Access to other lucrative investment opportunities</p>
</section>

<!-- 5 Rates -->
<section class="slide c2 r2">
  <div class="brand">Meridian Capital</div>
  <h2 class="title" style="left:18px;top:20px">Attractive Term Deposits</h2>
  <div class="rates">
    <div class="hd" style="left:0;width:61px;background:var(--navy);justify-content:flex-start;padding-left:7px">Term</div>
    <div class="hd" style="left:61px;width:61px;background:var(--sky)">Investment Size</div>
    <div class="hd" style="left:122px;width:62px;background:var(--grey)">Effective Annual Interest rate</div>
    <div class="row" style="top:69px"><span style="left:7px">3 months</span><span style="left:74px">$100k-$5m</span><span style="left:144px">5.95%</span></div>
    <div class="row" style="top:81px"><span style="left:7px">6 months</span><span style="left:74px">$100k-$5m</span><span style="left:144px">6.40%</span></div>
    <div class="row" style="top:93px"><span style="left:7px">12 months</span><span style="left:74px">$100k-$5m</span><span style="left:144px">6.95%</span></div>
    <div class="row" style="top:105px"><span style="left:7px">24 months</span><span style="left:74px">$100k-$5m</span><span style="left:144px">7.40%</span></div>
  </div>
  <p class="note-h">Note:</p>
  <div class="ic blue" style="left:210px;top:64px;width:14px;height:14px"><svg viewBox="0 0 10 10"><circle cx="5" cy="5" r="3.5" stroke="#fff" fill="none"/></svg></div>
  <p class="item" style="left:234px;top:62px;width:142px;font-size:5.8px">Interest begins accruing from the day the funds arrive in the Meridian Capital bank account</p>
  <div class="ic navy" style="left:210px;top:88px;width:14px;height:14px"><svg viewBox="0 0 10 10"><path d="M2 8L8 2" stroke="#fff" stroke-width="1.6"/></svg></div>
  <p class="item" style="left:234px;top:86px;width:142px;font-size:5.8px">Each deposit is structured as a loan to Meridian Capital Pty Ltd per the terms of the Deposit Agreement</p>
  <div class="ic blue" style="left:210px;top:122px;width:14px;height:14px"><svg viewBox="0 0 10 10"><circle cx="5" cy="5" r="3.5" stroke="#fff" fill="none"/></svg></div>
  <p class="item" style="left:234px;top:120px;width:142px;font-size:5.8px">Meridian Capital automatically deposits the interest in your account each calendar quarter on 1 January, 1 April, 1 July and 1 October</p>
  <div class="ic grey" style="left:210px;top:153px;width:14px;height:14px"><svg viewBox="0 0 10 10"><circle cx="5" cy="5" r="2.5" fill="#fff"/></svg></div>
  <p class="item" style="left:234px;top:151px;width:142px;font-size:5.8px">Deposit Agreements automatically roll over for a further term unless the depositor provides no less than 14 days notice prior to the end of the deposit term should they wish to withdraw part or all of their principal</p>
  <div class="foot"><div class="foot-bar"><span>Meridian Capital Pty Ltd ACN: 512 448 730</span><span>Head Office: Suite 8.04 Harbourview House, 220 Quay St, Melbourne 3008 VIC</span></div><div class="foot-num">5</div><div class="foot-end"></div></div>
</section>

<!-- 6 About -->
<section class="slide c3 r2">
  <h2 class="title" style="left:18px;top:20px">Who is Meridian Capital?</h2>
  <div class="ic blue" style="left:22px;top:55px;width:11px;height:11px"></div>
  <p class="item" style="left:37px;top:56px;font-size:5.8px">Melbourne-based finance company (ACN: 512 448 730)</p>
  <div class="ic navy" style="left:22px;top:74px;width:11px;height:11px"></div>
  <p class="item" style="left:37px;top:75px;font-size:5.8px">Provides short term finance to qualified businesses</p>
  <div class="ic grey" style="left:22px;top:94px;width:11px;height:11px"></div>
  <p class="item" style="left:37px;top:95px;font-size:5.8px">Parent company (Summit Holdings) established in 2009</p>
  <div class="ic blue" style="left:22px;top:113px;width:11px;height:11px"></div>
  <p class="item" style="left:37px;top:114px;font-size:5.8px">Meridian Capital brand launched late 2015</p>
  <div class="ic navy" style="left:22px;top:133px;width:11px;height:11px"></div>
  <p class="item" style="left:37px;top:130px;width:180px;font-size:5.8px">Representation in Melbourne, Singapore, London, New York &amp; Toronto</p>
  <div class="ic grey" style="left:22px;top:161px;width:11px;height:11px"></div>
  <p class="item" style="left:37px;top:162px;font-size:5.8px">Privy to unique high return investments due to industry position</p>
  <div class="ic blue" style="left:22px;top:181px;width:11px;height:11px"></div>
  <p class="item" style="left:37px;top:178px;width:195px;font-size:5.8px">Works alongside leading finance companies with high quality, pre-vetted deal flow</p>
  <div class="photo" style="left:246px;top:0;width:146px;height:210px;background:linear-gradient(170deg,#e4ebf2,#8aa0b7 55%,#4d5f73)" role="img" aria-label="Modern glass office building housing the head office"></div>
  <div class="abs" style="left:246px;top:148px;width:146px;height:48px;background:rgba(31,159,224,.88);color:#fff;text-align:center;padding-top:6px">
    <div style="font-size:8.5px">Meridian Capital's Head Office</div>
    <div style="font-size:6px;line-height:1.3;margin-top:1px">is located at Harbourview House, Quay Street (Victoria)</div>
  </div>
  <div class="brand light">Meridian Capital</div>
  <div class="foot"><div class="foot-bar"><span>Meridian Capital Pty Ltd ACN: 512 448 730</span><span>Head Office: Suite 8.04 Harbourview House, 220 Quay St, Melbourne 3008 VIC</span></div><div class="foot-num">6</div><div class="foot-end"></div></div>
</section>

<!-- 7 Testimonials -->
<section class="slide c1 r3">
  <div class="photo" style="left:0;top:0;width:150px;height:210px;background:linear-gradient(160deg,#eef1f4,#b9c3ce 55%,#2f3a4a)" role="img" aria-label="Smiling investor in a suit holding a tablet showing a growth chart"></div>
  <div class="brand">Meridian Capital</div>
  <h2 class="title" style="left:154px;top:20px">Happy Investors Globally</h2>
  <p class="quote" style="top:52px">"Well, I haven't been able to come up with a good reason to not invest. When I was searching for an investment with high rate of returns, I wasn't really optimistic that I would find one. I truly believe everything happens for good reason. This opportunity is perfect for me and know that I am working towards a ways of $500k AUS to you with a signed agreement!"
    <span class="by">- R. Castell (Tampa, Florida)</span>
    <span class="aside">(Note: this investor transferred $500,000 within 3 days of receiving this email having done extensive due diligence checks, and transferred a further $550,000 within 90 days of his initial deposit)</span></p>
  <p class="quote" style="top:138px">"Great News Daniel...we would like to roll all of it over for 24 months and we will send another deposit..."<span class="by">- K. Morton (Perth, Australia)</span></p>
  <p class="quote" style="top:170px">"I would like to reinvest at the 24 month option plus invest an additional amount"<span class="by">- L. Fraser (Adelaide, Australia)</span></p>
  <div class="foot"><div class="foot-bar"><span>Meridian Capital Pty Ltd ACN: 512 448 730</span><span>Head Office: Suite 8.04 Harbourview House, 220 Quay St, Melbourne 3008 VIC</span></div><div class="foot-num">7</div><div class="foot-end"></div></div>
</section>

<!-- 8 Team -->
<section class="slide c2 r3">
  <div class="brand">Meridian Capital</div>
  <h2 class="title" style="left:18px;top:20px">Experienced Senior Management</h2>
  <div class="mgr" style="left:12px"><div class="head" role="img" aria-label="Portrait photo"></div><p class="nm">Daniel Ashford</p><p class="rl">Managing Director</p><p class="lk">(View Profile)</p><ul><li>Former CEO of listed company</li><li>Extensive international investment experience</li><li>Bachelor of Laws and Commerce</li><li>Finalist, young leader award</li></ul></div>
  <div class="mgr" style="left:64px"><div class="head" role="img" aria-label="Portrait photo"></div><p class="nm">Rafiq Haddad</p><p class="rl">Managing Partner</p><p class="lk">(View Profile)</p><ul><li>Former business owner and operator</li><li>Manages daily investor operations</li><li>Digital strategy for business</li><li>BSc and BEng degrees</li></ul></div>
  <div class="mgr" style="left:117px"><div class="head" role="img" aria-label="Portrait photo"></div><p class="nm">Omar Salih</p><p class="rl">Senior Account Manager</p><p class="lk">(View Profile)</p><ul><li>10+ years financial services experience</li><li>Former stockbroker</li><li>Works with new and existing investors</li><li>Sources new opportunities</li></ul></div>
  <div class="mgr" style="left:170px"><div class="head" role="img" aria-label="Portrait photo"></div><p class="nm">Nikos Varela</p><p class="rl">Senior Account Manager</p><p class="lk">(View Profile)</p><ul><li>Regulated financial professional</li><li>Former head of equity derivatives</li><li>Works with new and existing investors</li><li>Sources new opportunities</li></ul></div>
  <div class="mgr" style="left:224px"><div class="head" role="img" aria-label="Portrait photo"></div><p class="nm">Graham Pellow</p><p class="rl">Senior Advisor &amp; UK Representative</p><p class="lk">(View Profile)</p><ul><li>Founder of a telecom group</li><li>Specialist in management and due diligence</li><li>Provides pre-vetted opportunities</li></ul></div>
  <div class="mgr" style="left:278px"><div class="head" role="img" aria-label="Portrait photo"></div><p class="nm">Peter Lindqvist</p><p class="rl">General Counsel</p><p class="lk">(View Profile)</p><ul><li>20+ years commercial law practice</li><li>10 years as company secretary</li><li>Advises on compliance and legal</li></ul></div>
  <div class="mgr" style="left:330px"><div class="head" role="img" aria-label="Portrait photo"></div><p class="nm">Sarah Wirananda</p><p class="rl">Finance Manager</p><p class="lk">(View Profile)</p><ul><li>CPA qualified accountant</li><li>Certified advisor</li><li>Manages company finances</li></ul></div>
  <div class="foot"><div class="foot-bar"><span>Meridian Capital Pty Ltd ACN: 512 448 730</span><span>Head Office: Suite 8.04 Harbourview House, 220 Quay St, Melbourne 3008 VIC</span></div><div class="foot-num">8</div><div class="foot-end"></div></div>
</section>

<!-- 9 Get started -->
<section class="slide c3 r3">
  <div class="start-bg"></div>
  <div class="abs" style="left:20px;top:44px;width:110px;text-align:center;font-size:8.5px;font-weight:600;color:var(--navy)">Meridian Capital</div>
  <div class="photo" style="left:28px;top:64px;width:106px;height:88px;background:linear-gradient(150deg,#e7e4dc,#b7ad9a 55%,#7e7466)" role="img" aria-label="Man reading on a tablet at home"></div>
  <h2 class="abs" style="left:170px;top:34px;font-size:16px;font-weight:400;color:#fff">Get Started</h2>
  <p class="abs" style="left:170px;top:58px;width:170px;font-size:6.2px;font-weight:600;color:#fff;line-height:1.3">To start earning a better rate of return on your money get started today!</p>
  <p class="abs" style="left:170px;top:80px;font-size:5.8px;color:var(--navy)">&gt;&gt; <u>Click here to Download a Deposit Agreement</u></p>
  <p class="abs" style="left:150px;top:121px;font-size:6px;font-weight:600;color:var(--ink)">Got Questions?</p>
  <div class="ic blue" style="left:150px;top:138px;width:14px;height:14px"></div>
  <div class="contact" style="left:170px;top:137px"><b>Making an Investment (AU or US)</b>Omar Salih<br><a>clientservices@meridiancap.com.au</a><br>+61 400 555 218</div>
  <div class="ic navy" style="left:262px;top:138px;width:14px;height:14px"></div>
  <div class="contact" style="left:282px;top:137px"><b>Making an Investment (UK or Europe)</b>Nikos Varela<br><a>clientservices@meridiancap.com.au</a><br>+44 7700 900 412</div>
  <div class="ic grey" style="left:150px;top:175px;width:14px;height:14px"></div>
  <div class="contact" style="left:170px;top:174px"><b>Customer Service Queries</b>Rafiq Haddad<br><a>manager@meridiancap.com.au</a><br>+61 (03) 9000 4417</div>
  <div class="ic blue" style="left:262px;top:175px;width:14px;height:14px"></div>
  <div class="contact" style="left:282px;top:174px"><b>Finance Queries</b>Sarah Wirananda<br><a>s.wirananda@meridiancap.com.au</a><br>+61 (03) 9000 4417</div>
  <div class="foot"><div class="foot-bar"><span>Meridian Capital Pty Ltd ACN: 512 448 730</span><span>Head Office: Suite 8.04 Harbourview House, 220 Quay St, Melbourne 3008 VIC</span></div><div class="foot-num">9</div><div class="foot-end"></div></div>
</section>

</body>
</html>
```